business card Kalvorin

Wee need a business card design for a new compagny based on Paris
We developped innovative a platform for selling services to refresh, beautify and develop its housing.
We would like a red logo on a black background
Te final design should communicate quality service, know-how, high-end

Target Market(s)

individuals

Industry/Entity Type

Business

```html
<!DOCTYPE html>
<html lang="en">
<head>
<meta charset="utf-8">
<title>Kalvorin business card</title>
<link href="https://fonts.googleapis.com/css2?family=Questrial&family=Arimo:wght@400&display=swap" rel="stylesheet">
<style>
  :root {
    --stage: #6b6b6b;
    --card-light: #ffffff;
    --card-dark: #000000;
    --brand-red: #f25c64;
    --wordmark-grey: #7d7d7d;
    --body-text: #4d4d4d;
  }
  * { margin: 0; padding: 0; box-sizing: border-box; }
  html, body {
    width: 1035px;
    height: 1200px;
    overflow: hidden;
    background: var(--stage);
  }
  .stage {
    position: relative;
    width: 1035px;
    height: 1200px;
  }
  .card {
    position: absolute;
    left: 136px;
    width: 762px;
    height: 436px;
    box-shadow: 3px 4px 10px rgba(0, 0, 0, 0.35);
  }
  .card--front { top: 131px; background: var(--card-light); }
  .card--back { top: 632px; background: var(--card-dark); }

  .brand {
    position: absolute;
    display: flex;
    align-items: center;
  }
  .brand__square {
    width: 75px;
    height: 75px;
    background: var(--brand-red);
    flex: none;
  }
  .brand__name {
    margin-left: 16px;
    font-family: "Questrial", "Century Gothic", sans-serif;
    font-size: 68px;
    line-height: 1;
    color: var(--wordmark-grey);
    letter-spacing: -0.5px;
  }
  .card--front .brand { left: 71px; top: 79px; }
  .card--back .brand { left: 210px; top: 181px; }

  .holder {
    position: absolute;
    left: 71px;
    top: 265px;
    font-family: "Questrial", "Century Gothic", sans-serif;
    color: var(--body-text);
  }
  .holder__name { font-size: 17px; line-height: 24px; }
  .holder__title { font-size: 14px; line-height: 22px; }

  .contact {
    position: absolute;
    left: 455px;
    top: 195px;
    font-family: "Arimo", Arial, sans-serif;
    font-size: 18px;
    line-height: 23px;
    color: var(--body-text);
    font-style: normal;
  }
  .contact__lines { margin-bottom: 23px; }
</style>
</head>
<body>
<main class="stage">
  <section class="card card--front" aria-label="Card front">
    <div class="brand">
      <span class="brand__square"></span>
      <span class="brand__name">Kalvorin</span>
    </div>
    <div class="holder">
      <p class="holder__name">Name xxxxxxxxxxxxxx</p>
      <p class="holder__title">xxxxxxxxxxxxxxxxxx</p>
    </div>
    <address class="contact">
      <p class="contact__lines">XXXX Lumen XXXX Court,<br>Near XXXX Square,<br>XXXX Avenue,<br>XXXXXkm XXXXX. 451 908</p>
      <p>M : 000-000-0427<br>info@kalvorin.fr<br>www.kalvorin.fr</p>
    </address>
  </section>

  <section class="card card--back" aria-label="Card back">
    <div class="brand">
      <span class="brand__square"></span>
      <span class="brand__name">Kalvorin</span>
    </div>
  </section>
</main>
</body>
</html>
```